I need a cover for a brochure made

I need a cover for a brochure. The dimensions are 8.25 wide and 5.25 high... I also need a .25 inch bleed outside of those dimensions.

I need it to look like a vintage photo album cover. In big words, I would like it to say "Family". Above it in smaller words "To our Harlow Fairway" ... making it look like the words are gold inlay or something.

I would like it kind of in the style of some of the attached maybe. Just vintage looking.

```html
<!DOCTYPE html>
<html lang="en">
<head>
<meta charset="utf-8">
<title>Family – Brochure Cover</title>
<link rel="stylesheet" href="https://fonts.googleapis.com/css2?family=Pinyon+Script&family=Fondamento:ital@1&display=swap">
<style>
  :root {
    --page: #ffffff;
    --leather: #2c0a16;
    --gold: #a58a16;
  }
  * { margin: 0; padding: 0; box-sizing: border-box; }
  html, body {
    width: 1200px;
    height: 854px;
    overflow: hidden;
    background: var(--page);
  }
  .canvas {
    position: relative;
    width: 1200px;
    height: 854px;
  }
  .album-cover {
    position: absolute;
    left: 296px;
    top: 228px;
    width: 579px;
    height: 368px;
    background: var(--leather);
  }
  .inlay-frame {
    position: absolute;
    left: 70px;
    top: 80px;
    width: 436px;
    height: 214px;
    border: 1.5px solid var(--gold);
  }
  .corner-ornament {
    position: absolute;
    width: 105px;
    height: 105px;
    background: radial-gradient(circle at var(--cx) var(--cy), rgba(165,138,22,0.55), rgba(165,138,22,0.12) 55%, rgba(165,138,22,0) 75%);
  }
  .corner-ornament.top-left     { left: 22px;  top: 22px;  --cx: 20%; --cy: 20%; }
  .corner-ornament.top-right    { left: 448px; top: 22px;  --cx: 80%; --cy: 20%; }
  .corner-ornament.bottom-left  { left: 22px;  top: 241px; --cx: 20%; --cy: 80%; }
  .corner-ornament.bottom-right { left: 448px; top: 241px; --cx: 80%; --cy: 80%; }
  .center-flourish {
    position: absolute;
    left: 219px;
    width: 141px;
    height: 12px;
    background: linear-gradient(90deg, rgba(165,138,22,0.15), rgba(165,138,22,0.6), rgba(165,138,22,0.15));
    border-radius: 6px;
  }
  .center-flourish.top    { top: 24px; }
  .center-flourish.bottom { top: 335px; }
  .dedication {
    position: absolute;
    left: 0;
    width: 100%;
    top: 94px;
    text-align: center;
    font-family: "Pinyon Script", cursive;
    font-size: 24px;
    color: var(--gold);
    line-height: 1;
  }
  .title {
    position: absolute;
    left: 0;
    width: 100%;
    top: 134px;
    text-align: center;
    font-family: "Fondamento", serif;
    font-style: italic;
    font-size: 126px;
    line-height: 1;
    color: var(--gold);
    letter-spacing: -1px;
  }
</style>
</head>
<body>
  <div class="canvas">
    <section class="album-cover">
      <div class="corner-ornament top-left" role="img" aria-label="Gold scrollwork corner ornament"></div>
      <div class="corner-ornament top-right" role="img" aria-label="Gold scrollwork corner ornament"></div>
      <div class="corner-ornament bottom-left" role="img" aria-label="Gold scrollwork corner ornament"></div>
      <div class="corner-ornament bottom-right" role="img" aria-label="Gold scrollwork corner ornament"></div>
      <div class="center-flourish top" role="img" aria-label="Gold centre flourish divider"></div>
      <div class="center-flourish bottom" role="img" aria-label="Gold centre flourish divider"></div>

      <div class="inlay-frame"></div>

      <p class="dedication">To our Harlow Fairway</p>
      <h1 class="title">Family</h1>
    </section>
  </div>
</body>
</html>
```